Local Swedish accounting firm needs a webpage design.

We need a logo design for an accounting firm based in Malmö, Sweden called "Veltrana". We provide a full range of accounting services and have worked closely with startups for many years.
We would like to see an design using the following color scheme.
https://huepiq.io/9b90ba-bfae48-646f58-2541b2-d56501
The design should communicate ease of use and financial safety.

Target Market(s)

We are an accounting firm so are clients are startups and small to medium sized companys

Industry/Entity Type

Accounting

Coding

Coded - Design and coding required

Number of Pages Required

1 page

Font styles to use
Sans Serif

```html
<!DOCTYPE html>
<html lang="sv">
<head>
<meta charset="utf-8">
<title>Veltrana – Our Services</title>
<link rel="stylesheet" href="https://fonts.googleapis.com/css2?family=Noto+Sans:wght@400;600;700&display=swap">
<style>
:root{
  --brand:#2541b2;
  --brand-deep:#2340b4;
  --ink:#2b3442;
  --text:#3a414c;
  --muted:#5b6270;
  --hero-bg:#f2f3f5;
  --blob:#f6f8fc;
  --accent:#d56501;
  --gold:#bfae48;
  --white:#ffffff;
}
*{margin:0;padding:0;box-sizing:border-box}
html,body{width:1200px;height:2188px;overflow:hidden}
body{position:relative;font-family:"Noto Sans",sans-serif;color:var(--text);background:var(--white)}
a{color:inherit;text-decoration:none}
.abs{position:absolute}
.top-rule{left:0;top:0;width:1200px;height:7px;background:var(--brand)}
.site-header{left:0;top:7px;width:1200px;height:70px;background:var(--white);box-shadow:0 2px 6px rgba(0,0,0,.05);z-index:3}
.brand-name{left:40px;top:14px;font-size:36px;font-weight:400;color:#111;letter-spacing:.5px}
.main-nav a{position:absolute;top:24px;font-size:14px;color:#3a3f48}
.main-nav a.active{color:var(--brand);border-bottom:1.5px solid var(--brand);padding:0 4px 3px}
.login-btn{left:1008px;top:14px;width:147px;height:40px;border-radius:20px;background:var(--brand);color:#fff;font-size:14px;font-weight:700;display:flex;align-items:center;justify-content:center}
.dropdown{left:468px;top:77px;width:240px;background:#fff;z-index:4;padding:3px 0}
.dropdown a{display:block;padding:0 17px;height:28px;line-height:28px;font-size:12.5px;color:#333;border-bottom:1px solid #f0f0f0}
.dropdown a:last-child{border-bottom:none}
.hero{left:0;top:77px;width:1200px;height:345px;background:var(--hero-bg)}
.hero-title{left:137px;top:245px;font-size:38px;font-weight:700;color:var(--brand)}
.btn{background:var(--brand);color:#fff;border-radius:20px;display:flex;align-items:center;justify-content:center;font-weight:700;font-size:14px}
.hero-cta{left:137px;top:322px;width:147px;height:40px}
.hero-art{left:672px;top:128px;width:460px;height:300px;border-radius:8px 8px 120px 120px;background:linear-gradient(135deg,#e6ecfb 0%,#cfdcf6 55%,#f4e7b8 100%)}
.blob{left:-40px;top:600px;width:640px;height:920px}
.section-title{left:0;top:496px;width:1200px;text-align:center;font-size:32px;font-weight:700;color:var(--ink)}
.section-lead{left:250px;top:562px;width:700px;text-align:center;font-size:19px;line-height:26px;color:#444}
.service .icon{position:absolute;width:66px;height:76px}
.service h3{position:absolute;font-size:23.5px;font-weight:700;color:var(--ink);line-height:28px}
.service p{position:absolute;font-size:16px;line-height:28.2px;color:var(--text)}
.read-more{position:absolute;font-size:19px;color:var(--brand);border-bottom:2px solid var(--brand);padding-bottom:6px}
.site-footer{left:0;top:1802px;width:1200px;height:378px;background:var(--brand-deep);color:#dfe5ff}
.footer-logo{left:141px;top:40px;width:115px;height:72px;background:#fff;color:var(--brand);font-size:15px;display:flex;align-items:center;justify-content:center}
.footer-contact{left:139px;top:137px;font-size:16px;line-height:29px;color:#d6ddfa}
.footer-col h4{font-size:16px;font-weight:700;color:#fff;line-height:29px}
.footer-col a{display:block;font-size:16px;line-height:29px;color:#e6ebff}
.member{left:932px;top:48px;width:210px;font-size:16px;line-height:22px;color:#e6ebff}
.badge{left:962px;top:124px;width:40px;height:40px;background:var(--gold);border-radius:4px}
.footer-rule{left:0;top:328px;width:1200px;height:1px;background:rgba(255,255,255,.15)}
.copyright{left:133px;top:344px;font-size:12px;color:#e6ebff}
.legal{left:915px;top:343px;font-size:11px;color:#e6ebff}
.accent-strip{left:0;top:2180px;width:1200px;height:8px;background:var(--accent)}
</style>
</head>
<body>
<div class="abs top-rule"></div>

<header class="abs site-header">
  <div class="abs brand-name">VELTRANA</div>
  <nav class="main-nav">
    <a style="left:402px">Startsida</a>
    <a style="left:481px" class="active">Våra tjänster</a>
    <a style="left:594px">Om Veltrana</a>
    <a style="left:698px">För entreprenörer</a>
    <a style="left:840px">GDPR</a>
    <a style="left:904px">Kontakt</a>
  </nav>
  <a class="abs login-btn">Kundinloggning</a>
</header>

<section class="abs hero">
  <h1 class="abs hero-title" style="top:168px">Our Services</h1>
  <a class="abs btn hero-cta" style="top:245px">Contact Us</a>
  <div class="abs hero-art" style="top:51px" role="img" aria-label="Illustration of a tax form, calendar, calculator, gold coins and a potted plant"></div>
</section>

<nav class="abs dropdown">
  <a>Accounting</a>
  <a>Payroll Management</a>
  <a>Annual accounts and declarations</a>
  <a>Project accounting</a>
  <a>Financial management</a>
  <a>Finance department</a>
</nav>

<svg class="abs blob" viewBox="0 0 640 920" aria-hidden="true">
  <path d="M40 60 C120 10 200 -10 260 80 C300 150 330 260 440 250 C560 240 640 330 600 470 C560 600 520 640 560 760 C600 880 420 930 280 880 C160 840 60 900 40 860 Z" fill="var(--blob)"/>
</svg>

<h2 class="abs section-title">Accounting &amp; Taxation Specialists</h2>
<p class="abs section-lead">Lorem ipsum dolor sit amet, consectetur adipiscing elit, sed do eiusmod tempor incididunt ut labore et dolore magna aliqua.</p>

<!-- Accounting -->
<div class="service">
  <svg class="icon" style="left:110px;top:672px" viewBox="0 0 66 76" fill="none" stroke="var(--brand)" stroke-width="3.5" stroke-linecap="round">
    <rect x="4" y="4" width="58" height="68" rx="5"/>
    <path d="M26 16c-2-3-10-3-10 2s10 3 10 8-8 5-10 2M21 12v20M34 20h14M34 28h14M16 44h32M16 54h32"/>
  </svg>
  <h3 style="left:199px;top:667px">Accounting</h3>
  <p style="left:199px;top:702px;width:340px">Om du vill ägna dig helhjärtat åt din affärsverksamhet är hjälp med den löpande redovisningen ett gott råd. Då behöver du inte lägga tid på vare sig administration, redovisning eller att hålla dig uppdaterad om regel-förändringar. Det gör vi åt dig.</p>
  <a class="read-more" style="left:199px;top:896px;width:114px">Read more</a>
</div>

<!-- Payroll -->
<div class="service">
  <svg class="icon" style="left:617px;top:664px" viewBox="0 0 66 76" fill="none" stroke="var(--brand)" stroke-width="4" stroke-linecap="round">
    <path d="M14 56A29 29 0 1 1 52 56"/>
    <path d="M40 22c-3-4-14-4-14 3s14 4 14 11-11 6-14 2M33 16v32M12 66h42"/>
  </svg>
  <h3 style="left:705px;top:667px">Payroll management</h3>
  <p style="left:705px;top:702px;width:370px">En genomtänkt grundstruktur för rutiner, redovisning och datainformation frigör mängder med tid. Värdefull tid som kan användas på ett mer lönsamt sätt i företaget. Vi kan hjälpa dig att förbättra företagets rutiner. Vi skapar en stabil grundstruktur för ett effektivt ekonomiflöde.</p>
  <a class="read-more" style="left:705px;top:896px;width:117px">Read more</a>
</div>

<!-- Project accounting -->
<div class="service">
  <svg class="icon" style="left:106px;top:996px" viewBox="0 0 66 76" fill="none" stroke="var(--brand)" stroke-width="3.5" stroke-linejoin="round" stroke-linecap="round">
    <path d="M62 4C44 4 30 14 22 30l14 14C52 36 62 22 62 4Z"/>
    <path d="M22 30 8 32 2 40l14 2M36 44l-2 14-8 6-2-14M18 46 8 56"/>
    <circle cx="44" cy="22" r="5"/>
  </svg>
  <h3 style="left:195px;top:996px">Project accounting</h3>
  <p style="left:195px;top:1032px;width:340px">Ekonomisk information svart på vitt är oftast bästa beslutsunderlaget. Beslut baserade på antaganden håller sällan i längden. Säkra och tydliga beslutsunderlag ger dig möjlighet att förutse effekterna av olika handlingsalternativ och utveckla företaget i rätt riktning.</p>
  <a class="read-more" style="left:195px;top:1252px;width:113px">Read more</a>
</div>

<!-- Financial management -->
<div class="service">
  <svg class="icon" style="left:612px;top:994px" viewBox="0 0 66 76" fill="none" stroke="var(--brand)" stroke-width="3.5" stroke-linecap="round" stroke-linejoin="round">
    <path d="M24 28H6v38h54V34"/>
    <path d="M50 4l8 8-22 22-11 3 3-11Z"/>
    <path d="M16 52h34M16 60h34"/>
  </svg>
  <h3 style="left:700px;top:996px">Financial management</h3>
  <p style="left:700px;top:1032px;width:380px">Som din externa ekonomiavdelning tillför vi ekonomisk kompetens inom<br>alla områden och tar ett helhetsansvar för ekonomifunktionen. Du får någon som hjälper dig att ha kontroll över den operativa verksamheten, som reagerar och ger goda råd på vägen.</p>
  <a class="read-more" style="left:700px;top:1226px;width:118px">Read more</a>
</div>

<!-- Annual accounts -->
<div class="service">
  <svg class="icon" style="left:100px;top:1354px" viewBox="0 0 66 76" fill="none" stroke="var(--brand)" stroke-width="3.5" stroke-linecap="round" stroke-linejoin="round">
    <path d="M12 30H4V4h58v26h-8"/>
    <path d="M12 12h42v54l-6-4-6 4-6-4-6 4-6-4-6 4-6-4Z"/>
    <rect x="24" y="24" width="18" height="14"/>
    <path d="M24 48h18"/>
  </svg>
  <h3 style="left:195px;top:1354px;width:340px">Annual accounts and declarations</h3>
  <p style="left:195px;top:1413px;width:340px">Om du vill ägna dig helhjärtat åt din affärsverksamhet är hjälp med den löpande redovisningen ett gott råd. Då behöver du inte lägga tid på vare sig administration, redovisning eller att hålla dig uppdaterad om regel-förändringar. Det gör vi åt dig.</p>
  <a class="read-more" style="left:195px;top:1582px;width:113px">Read more</a>
</div>

<!-- Finance department -->
<div class="service">
  <svg class="icon" style="left:617px;top:1356px" viewBox="0 0 66 76" fill="none" stroke="var(--brand)" stroke-width="3.5" stroke-linecap="round" stroke-linejoin="round">
    <path d="M24 28H6v38h54V34"/>
    <path d="M50 4l8 8-22 22-11 3 3-11Z"/>
    <path d="M16 52h34M16 60h34"/>
  </svg>
  <h3 style="left:700px;top:1354px">Finance department</h3>
  <p style="left:700px;top:1389px;width:370px">En genomtänkt grundstruktur för rutiner, redovisning och datainformation frigör mängder med tid. Värdefull tid som kan användas på ett mer lönsamt sätt i företaget. Vi kan hjälpa dig att förbättra företagets rutiner. Vi skapar en stabil grundstruktur för ett effektivt ekonomiflöde.</p>
  <a class="read-more" style="left:700px;top:1582px;width:118px">Read more</a>
</div>

<footer class="abs site-footer">
  <div class="abs footer-logo">VELTRANA</div>
  <div class="abs footer-contact">
    Lindvägen 14<br>211 45 Malmö<br><br>
    Tel:&nbsp; 040-55 21 07<br>
    Fax: (86) 0769-55501234<br>
    Email: info@veltrana.se
  </div>
  <div class="abs footer-col" style="left:413px;top:37px">
    <h4>Our Services</h4>
    <a>Accounting</a>
    <a>Payroll Management</a>
    <a>Annual Accounts &amp; Declarations</a>
    <a>Project Accounting</a>
    <a>Financial Management</a>
    <a>Finance Department</a>
  </div>
  <div class="abs footer-col" style="left:736px;top:37px">
    <h4>Company</h4>
    <a>About Us</a>
    <a>Contact Us</a>
    <a>Resources</a>
    <a>Guidance</a>
  </div>
  <div class="abs member">Member of Nordic Guild of Bookkeeping Advisors</div>
  <div class="abs badge" role="img" aria-label="Membership badge"></div>
  <div class="abs footer-rule"></div>
  <div class="abs copyright">Copyright © 2020 Veltrana AB. All rights reserved.</div>
  <div class="abs legal">Privacy Policy | Terms &amp; Conditions</div>
</footer>
<div class="abs accent-strip"></div>
</body>
</html>
```